IT Company Business Card design

Brisk Node is a new computer solutions business focusing on setting up servers and computer systems for small to medium sized businesses.

A business client will either request a solution, or support for a current system and we will turn up on site to provide these services.

We are bast in Christchurch, New Zealand.

We are looking for unique business card's that stand out and show off the business in a professional light.

Open to all idea's etc.

Industry/Entity Type

Computer

Requirements
Must have
• Business Logo (AI file attached)
Employee Name
Business title
Business landline number
Cell phone number
Email
Web URL
Nice to have
• Could be nice to have some keywords (possibly on the back) such as:

Business IT solutions
Network installations
Phone solutions
Server management
Software diagnostics

The above is not needed, just an idea.

```html
<!DOCTYPE html>
<html lang="en">
<head>
<meta charset="utf-8">
<title>Brisk Node – Business Card</title>
<link rel="stylesheet" href="https://fonts.googleapis.com/css2?family=Questrial&display=swap">
<style>
  :root {
    --page: #d9dadc;
    --card: #ffffff;
    --card-shade: #eceef0;
    --blue: #1a64a8;
    --blue-dark: #0f4f8d;
    --blue-light: #3d8cc8;
    --strip: #4a8fc6;
    --grey-bar: #7d7f82;
    --ink: #222428;
    --ink-soft: #5a5d62;
  }
  * { box-sizing: border-box; margin: 0; padding: 0; }
  html, body { width: 1200px; height: 871px; overflow: hidden; }
  body {
    background: var(--page);
    font-family: "Questrial", "Century Gothic", sans-serif;
    display: flex;
    align-items: center;
    justify-content: center;
    gap: 60px;
  }
  .card {
    position: relative;
    width: 520px;
    height: 298px;
    background: linear-gradient(160deg, var(--card) 0%, var(--card-shade) 100%);
    box-shadow: 0 6px 18px rgba(0,0,0,0.18);
    overflow: hidden;
  }

  /* Back card */
  .back .name-bar {
    position: absolute; left: 186px; top: 0;
    width: 22px; height: 96px;
    background: var(--grey-bar);
  }
  .back .identity {
    position: absolute; right: 318px; top: 112px;
    text-align: right;
  }
  .back .person-name { color: var(--blue-light); font-size: 19px; letter-spacing: 0.3px; }
  .back .person-title, .back .person-company { color: var(--ink-soft); font-size: 10px; line-height: 1.25; }
  .back .icon-strip {
    position: absolute; left: 222px; top: 24px;
    width: 26px; height: 250px;
    background: var(--strip);
    display: flex; flex-direction: column; align-items: center;
    padding-top: 24px; gap: 14px;
  }
  .back .icon-strip svg { width: 14px; height: 14px; }
  .back .contact-list {
    position: absolute; left: 258px; top: 24px;
    list-style: none; color: var(--ink); font-size: 15px;
  }
  .back .contact-list .address { font-size: 11.5px; line-height: 1.22; color: var(--ink-soft); margin-bottom: 4px; }
  .back .contact-list li { height: 28px; line-height: 28px; }
  .back .contact-list li.address { height: auto; line-height: 1.22; }
  .back .footer-band {
    position: absolute; left: 0; right: 0; bottom: 0; height: 24px;
    background: var(--blue);
    color: #fff; font-size: 12px; letter-spacing: 1px;
    display: flex; align-items: center; padding-left: 258px;
  }

  /* Front card */
  .front .brand {
    position: absolute; left: 0; right: 0; top: 98px;
    display: flex; align-items: center; justify-content: center; gap: 24px;
  }
  .front .brand-dot {
    width: 78px; height: 78px; border-radius: 50%;
    background: var(--blue);
  }
  .front .brand-divider { width: 1px; height: 84px; background: #9a9ca0; }
  .front .brand-name {
    color: var(--ink); font-size: 36px; letter-spacing: 8px; text-transform: uppercase;
  }
  .front .footer-band {
    position: absolute; left: 0; right: 0; bottom: 0; height: 38px;
    background: linear-gradient(180deg, var(--blue) 0%, var(--blue-dark) 100%);
    color: #fff; font-size: 14px; letter-spacing: 0.5px;
    display: flex; align-items: center; padding-left: 60px;
  }
</style>
</head>
<body>

<section class="card back">
  <div class="name-bar"></div>
  <div class="identity">
    <p class="person-name">Tane Whiri</p>
    <p class="person-title">Director</p>
    <p class="person-company">Harbour Grid</p>
  </div>
  <div class="icon-strip">
    <svg viewBox="0 0 14 14" aria-hidden="true"><path d="M7 1a4 4 0 0 0-4 4c0 3 4 8 4 8s4-5 4-8a4 4 0 0 0-4-4z" fill="#fff"/><circle cx="7" cy="5" r="1.4" fill="#4a8fc6"/></svg>
    <svg viewBox="0 0 14 14" aria-hidden="true" style="margin-top:12px"><rect x="3.5" y="1" width="7" height="12" rx="1.2" fill="none" stroke="#fff" stroke-width="1.3"/><circle cx="7" cy="11" r="0.8" fill="#fff"/></svg>
    <svg viewBox="0 0 14 14" aria-hidden="true"><path d="M1 5c0-2 12-2 12 0v1.5H10V5H4v1.5H1z" fill="#fff"/><rect x="3" y="7" width="8" height="5.5" rx="1" fill="#fff"/></svg>
    <svg viewBox="0 0 14 14" aria-hidden="true"><rect x="1" y="3" width="12" height="8" fill="none" stroke="#fff" stroke-width="1.3"/><path d="M1 3l6 5 6-5" fill="none" stroke="#fff" stroke-width="1.3"/></svg>
    <svg viewBox="0 0 14 14" aria-hidden="true"><circle cx="7" cy="7" r="5.5" fill="none" stroke="#fff" stroke-width="1.2"/><ellipse cx="7" cy="7" rx="2.3" ry="5.5" fill="none" stroke="#fff" stroke-width="1"/><path d="M1.5 7h11" stroke="#fff" stroke-width="1"/></svg>
  </div>
  <ul class="contact-list">
    <li class="address">2nd floor, Oriel House,<br>14 Cashel Lane, Riccarton,<br>Christchurch, New Zealand.</li>
    <li>64.21.555.0142</li>
    <li>64.3.555.1950</li>
    <li>64.3.555.0055</li>
    <li>tane.whiri@harbourgrid.co</li>
    <li>www.harbourgrid.co</li>
  </ul>
  <div class="footer-band">WORK &nbsp;|&nbsp; WORK &nbsp;|&nbsp; WORK</div>
</section>

<section class="card front">
  <div class="brand">
    <span class="brand-dot"></span>
    <span class="brand-divider"></span>
    <span class="brand-name">Brisk Node</span>
  </div>
  <div class="footer-band">www.brisknode.co</div>
</section>

</body>
</html>
```